依頼詳細
お客様に見積もり・図面などを提出する時に使用する封筒です。使用用途は幅広く、その他にも取引業者さまへのお手紙を出す時にも使います。

弊社は新築住宅・リフォーム工事を施工しているため、どちらのお客様にも使用できるよう、シンプルでかっこいいデザインをもとめています。
裏ありでも、なしでも構いません。

ロゴ添付しましたが、使用してもしなくても、構いません。

参考に弊社のホームページです

URL: https://www.bluecrestyuzawa.jp/
記載項目
北森燃料株式会社 住宅事業部 BLUE CREST
■下沢田ショールーム
〒048-2207
青森県三戸郡五戸町下沢田岡平34-8
■住宅事業部 本店事務所
〒048-2208
青森県三戸郡五戸町鶴間台柳原下平地52-6

※ここより下は2店の共通事項になります↓
TEL: 0178-94-7201 FAX: 0178-94-7216
Email: bluecrest.info@kitamori-nenryo.com
希望イメージ
シンプル 複雑
単色 カラフル
暗い 明るい
日常 高級
遊び心 厳粛
未来的 伝統的
女性的 男性的
希望する色
グレー系
納品ファイル
• イラストレーター形式 (.ai)
補足説明
ツバサプリント様にすぐ入稿できる形での納品をお願い致します。
※継続依頼あります。宜しくお願い致します。
■ 選んだ理由

『シンプルでかっこいい』という依頼通りのデザインでとても気に入りました。沢山デザインして頂き、ありがとうございます。丁寧で誠実な対応に感謝です。是非又何かありましたら、宜しくお願い致します。

■ 提案者全員のお礼・コメント

今回、報酬が安価に関わらず、沢山のランサー様が素敵なデザインを作成して頂きました!本当にありがとうございました。

```html
<!DOCTYPE html>
<html lang="ja">
<head>
<meta charset="UTF-8">
<title>BLUE CREST 封筒デザイン</title>
<link href="https://fonts.googleapis.com/css2?family=Noto+Sans+JP:wght@400;500;700&family=Montserrat:wght@500;600&display=swap" rel="stylesheet">
<style>
  :root {
    --page: #ffffff;
    --flap: #8e908f;
    --flap-edge: #7f817f;
    --body: #c9ccc9;
    --brand-green: #1f5b46;
    --ink: #333635;
    --ink-soft: #4a4d4c;
    --rule: #555857;
    --white: #f4f5f4;
  }
  * { margin: 0; padding: 0; box-sizing: border-box; }
  html, body { width: 846px; height: 1200px; overflow: hidden; background: var(--page); }
  body { font-family: "Noto Sans JP", sans-serif; color: var(--ink); }

  .envelope {
    position: absolute;
    left: 62px; top: 68px;
    width: 722px; height: 1092px;
  }
  .envelope__flap {
    position: absolute; left: 0; top: 0;
    width: 722px; height: 90px;
    background: var(--flap);
    border-top: 6px solid var(--flap-edge);
  }
  .flap-mark {
    position: absolute; left: 50%; top: 16px;
    transform: translateX(-50%);
    display: flex; align-items: center; gap: 5px;
    color: var(--white);
    font-family: "Montserrat", sans-serif;
    font-weight: 500; font-size: 8px; letter-spacing: 2px;
  }
  .flap-mark__square { width: 7px; height: 7px; background: var(--white); }

  .envelope__body {
    position: absolute; left: 0; top: 90px;
    width: 722px; height: 1002px;
    background: var(--body);
  }

  .brand {
    position: absolute; left: 90px; top: 260px;
    display: flex; align-items: center; gap: 10px;
    color: var(--brand-green);
    font-family: "Montserrat", sans-serif;
    font-weight: 600; font-size: 24px; letter-spacing: 3px;
  }
  .brand__square { width: 18px; height: 18px; background: var(--brand-green); }

  .sender {
    position: absolute; left: 20px; right: 20px; top: 890px;
  }
  .sender__name {
    font-size: 15px; font-weight: 700; letter-spacing: 1.5px;
    padding-bottom: 6px;
    border-bottom: 1px solid var(--rule);
  }
  .sender__name .en { font-family: "Montserrat", sans-serif; font-weight: 600; letter-spacing: 2px; margin-left: 6px; }
  .sender__row {
    display: flex; align-items: baseline; gap: 18px;
    margin-top: 7px; font-size: 10px; font-weight: 500;
  }
  .sender__row .email { font-size: 7px; color: var(--ink-soft); }
  .sender__offices { display: flex; gap: 22px; margin-top: 8px; font-size: 6.5px; line-height: 1.8; color: var(--ink-soft); }
  .offices__labels { font-weight: 500; color: var(--ink); }
  .sender__url {
    margin-top: 14px; font-family: "Montserrat", sans-serif;
    font-size: 8px; font-weight: 500; color: var(--brand-green);
  }
</style>
</head>
<body>
  <div class="envelope">
    <div class="envelope__flap">
      <div class="flap-mark"><span class="flap-mark__square"></span>BLUE CREST</div>
    </div>
    <div class="envelope__body">
      <div class="brand"><span class="brand__square"></span>BLUE CREST</div>

      <div class="sender">
        <p class="sender__name">北森燃料株式会社 住宅事業部<span class="en">BLUE CREST</span></p>
        <p class="sender__row">
          <span>TEL.0178-94-7201　FAX.0178-94-7216</span>
          <span class="email">Email: bluecrest.info@kitamori-nenryo.com</span>
        </p>
        <div class="sender__offices">
          <div class="offices__labels">
            <p>■下沢田ショールーム</p>
            <p>■住宅事業部 本店事務所</p>
          </div>
          <div class="offices__addresses">
            <p>〒048-2207 青森県三戸郡五戸町下沢田岡平34-8</p>
            <p>〒048-2208 青森県三戸郡五戸町鶴間台柳原下平地52-6</p>
          </div>
        </div>
        <p class="sender__url">https://www.bluecrestyuzawa.jp/</p>
      </div>
    </div>
  </div>
</body>
</html>
```